Project Name Card Design, Verdano Cargo

Company Profile
Verdano Cargo Sdn Bhd is a well-established and experienced freight forwarder in Kuala Lumpur, Malaysia. We specialize in air and sea forwarding, Custom Brokerage and regulatory compliance services, inland transportation, overseas freighting and warehousing and distribution management. With our dedicated qualified and experienced professionals, we are fully committed to serving our clients.

Our Mission
Based on the motto “Quick, Reliable and Polite”, Verdano Cargo is dedicated to upholding the following three points corporate philosophy:1. Adhering to the principle that “the customer always comes first”.2. Contributing to the development of the local community.3. Making it our duty to be responsible and sincere.

Our Edge
• One-Stop Logistics Solutions
• Extensive Network Throughout Malaysia
• Highly Qualified and Experienced Pool of Professionals
• Comprehensive IT Solutions
• Innovative and Customer-focused Solutions
• Flexible and Consistent in Managing Exceptions
• Total Supply Chain Visibility

Target Market : We sell the logistics services to all the industry in Malaysia. (One Stop Logistics Solutions)

Business Card Detail : I would like to see the logo on the front with the general info.

Must Haves :
1) Name, Title, Office, Cell, Fax, Email, Address, Website
2) Must have complete company name show as : Verdano Cargo Sdn Bhd
3) Must have company registration no, show as : 8057146-P

Nice to Haves : Modern Design Business Card

Target Market(s)

We sell the logistics services to all the industry in Malaysia. (One Stop Logistics Solutions)

Contact Information for Business Card

I would like to see the logo on the front with the general info.

Colors

Designer to choose colors to be used in the design.

Requirements
Must have
• 1) Name, Title, Office, Cell, Fax, Email, Address, Website
• 2) Must have complete company name show as : Verdano Cargo Sdn Bhd
• 3) Must have company registration no, show as : 8057146-P
Nice to have
• Modern Design Business Card
Should not have
• Nil

```html
<!DOCTYPE html>
<html lang="en">
<head>
<meta charset="utf-8">
<title>Verdano Cargo – Name Card</title>
<link rel="stylesheet" href="https://fonts.googleapis.com/css2?family=Lato:wght@400;700&family=Michroma&display=swap">
<style>
  :root {
    --stage: #1b1b1d;
    --card: #141416;
    --card-edge: #262629;
    --silver: #d4d6d9;
    --text: #e6e6e6;
    --muted: #9a9ca0;
    --blue: #1e8fd6;
    --blue-deep: #1565a8;
    --rule: #3a3b3f;
  }
  * { margin: 0; padding: 0; box-sizing: border-box; }
  html, body { width: 1200px; height: 900px; overflow: hidden; }
  body {
    background: var(--stage);
    font-family: "Lato", Arial, sans-serif;
    color: var(--text);
    position: relative;
  }
  .card {
    position: absolute;
    width: 560px;
    height: 320px;
    background: var(--card);
    border: 1px solid var(--card-edge);
    border-radius: 22px;
    box-shadow: 0 18px 40px rgba(0,0,0,.55);
  }
  /* Back of card */
  .card--back { left: 150px; top: 110px; }
  .back-mark {
    position: absolute; left: 0; right: 0; top: 92px;
    display: flex; align-items: center; justify-content: center; gap: 16px;
  }
  .back-mark .mark-circle {
    width: 54px; height: 54px; border-radius: 50%;
    border: 3px solid var(--silver);
  }
  .back-mark .company-name {
    font-family: "Lato", Arial, sans-serif;
    font-weight: 700; font-size: 30px; letter-spacing: 3px;
    color: var(--silver); text-transform: uppercase;
  }
  .tagline {
    position: absolute; left: 0; right: 0; bottom: 52px;
    text-align: center; font-size: 14px; letter-spacing: 1px;
    color: var(--text);
  }

  /* Front of card */
  .card--front { left: 490px; top: 470px; }
  .brand {
    position: absolute; right: 34px; top: 30px;
    display: flex; align-items: center; gap: 14px;
  }
  .brand .mark-circle {
    width: 48px; height: 48px; border-radius: 50%;
    border: 3px solid var(--blue-deep);
  }
  .brand .divider { width: 1px; height: 56px; background: var(--blue-deep); }
  .brand .company-name {
    font-family: "Lato", Arial, sans-serif; font-weight: 700;
    font-size: 25px; letter-spacing: 3px; color: var(--blue);
    text-transform: uppercase; line-height: 1;
  }
  .brand .reg-no { font-size: 13px; color: var(--text); margin-top: 8px; letter-spacing: .3px; }
  .brand-rule {
    position: absolute; left: 290px; right: 34px; top: 104px;
    height: 1px; background: var(--rule);
  }
  .address {
    position: absolute; right: 34px; top: 124px;
    text-align: right; font-size: 12.5px; line-height: 1.35; color: var(--text);
  }
  .person { position: absolute; left: 32px; top: 186px; }
  .person-name {
    font-family: "Michroma", "Lato", sans-serif;
    font-size: 18px; color: var(--blue); letter-spacing: 1px; line-height: 1.1;
  }
  .person-title { font-size: 13px; color: var(--text); }
  .person-rule {
    position: absolute; left: 178px; width: 130px; top: 198px;
    height: 1px; background: var(--rule);
  }
  .contacts {
    position: absolute; left: 32px; top: 236px;
    list-style: none; font-size: 12.5px; line-height: 15.5px;
  }
  .contacts li { display: flex; align-items: center; gap: 7px; }
  .contacts svg { width: 11px; height: 11px; fill: var(--blue); flex: none; }
</style>
</head>
<body>

<section class="card card--back" aria-label="Card back">
  <div class="back-mark">
    <span class="mark-circle"></span>
    <span class="company-name">Verdano Cargo</span>
  </div>
  <p class="tagline">ONE STOP LOGISTICS SPECIALIST</p>
</section>

<section class="card card--front" aria-label="Card front">
  <div class="brand">
    <span class="mark-circle"></span>
    <span class="divider"></span>
    <div>
      <div class="company-name">Verdano Cargo</div>
      <div class="reg-no">Registration No: 8057146-P</div>
    </div>
  </div>
  <div class="brand-rule"></div>

  <address class="address" style="font-style:normal">
    Verdano Cargo Sdn Bhd<br>
    No.27B, 2nd Floor, Jalan Seri Mutiara<br>
    4/KS2, 41150 Klang<br>
    Taman Seri Mutiara,<br>
    Selangor Darul Ehsan, Malaysia
  </address>

  <div class="person">
    <div class="person-name">DANIEL TAN</div>
    <div class="person-title">Managing Director</div>
  </div>
  <div class="person-rule"></div>

  <ul class="contacts">
    <li><svg viewBox="0 0 24 24"><path d="M6.6 10.8a15 15 0 0 0 6.6 6.6l2.2-2.2a1 1 0 0 1 1-.25 11.4 11.4 0 0 0 3.6.57 1 1 0 0 1 1 1V20a1 1 0 0 1-1 1A17 17 0 0 1 3 4a1 1 0 0 1 1-1h3.5a1 1 0 0 1 1 1c0 1.25.2 2.45.57 3.6a1 1 0 0 1-.25 1z"/></svg>(+6012) 555 0172</li>
    <li><svg viewBox="0 0 24 24"><path d="M7 1h10a2 2 0 0 1 2 2v18a2 2 0 0 1-2 2H7a2 2 0 0 1-2-2V3a2 2 0 0 1 2-2zm0 3v14h10V4zm5 15.5a1 1 0 1 0 0 2 1 1 0 0 0 0-2z"/></svg>(+603) 3350 0186 / 0187</li>
    <li><svg viewBox="0 0 24 24"><path d="M6 2h9l3 3v4H6zm-2 8h16a2 2 0 0 1 2 2v6h-4v4H6v-4H2v-6a2 2 0 0 1 2-2zm4 6v4h8v-4z"/></svg>(+603) 3350 0188</li>
    <li><svg viewBox="0 0 24 24"><path d="M2 5h20v14H2zm2 2v.5l8 5.5 8-5.5V7z"/></svg>daniel.tan@verdanocargo.com.my</li>
    <li><svg viewBox="0 0 24 24"><circle cx="12" cy="12" r="10"/></svg>www.verdanocargo.com.my</li>
  </ul>
</section>

</body>
</html>
```